Corvena Hotel, city center modern minimal hotel operating all year round, on Rhodes island Greece

city, modern ,all year operating hotel

Target Market(s)

tourists, business agents

Industry/Entity Type

tourism

Coding

Coded - Design and coding required

Number of Pages Required

2 page

Requirements
Must have
• room type photos and descriptions, amenities individual listing (graphic), comments sections, map driving location details
Nice to have
• gallery section, modern and minimal design, amenities section, individual room type descriptions, photos and facilities

```html
<!DOCTYPE html>
<html lang="en">
<head>
<meta charset="utf-8">
<title>Corvena Hotel — About Us</title>
<link href="https://fonts.googleapis.com/css2?family=Barlow:wght@400;500;600&family=Cabin:wght@400;500&display=swap" rel="stylesheet">
<style>
:root{
  --gold:#bd9343;
  --ink:#14161a;
  --dark:#0f1317;
  --text:#3a3d42;
  --foot-text:#d6d8dc;
  --white:#ffffff;
  --line:rgba(255,255,255,.12);
}
*{margin:0;padding:0;box-sizing:border-box}
html,body{width:1200px;height:2970px;overflow:hidden}
body{position:relative;background:var(--white);font-family:"Cabin",sans-serif;color:var(--text)}
.heading{font-family:"Barlow",sans-serif;font-weight:400;color:var(--ink)}

/* hero */
.hero{position:absolute;left:0;top:0;width:1200px;height:396px;background:linear-gradient(100deg,#1a1d22 0%,#2c2e33 45%,#26282c 70%,#1c1e22 100%)}
.nav-bar{position:absolute;left:0;top:0;width:1200px;height:105px;border-bottom:1px solid var(--line)}
.brand{position:absolute;display:flex;align-items:center;gap:12px;font-family:"Barlow",sans-serif;font-size:30px;font-weight:500;color:var(--white);letter-spacing:1px;white-space:nowrap}
.hero .brand{left:50px;top:34px}
.brand-mark{width:26px;height:26px;background:var(--gold)}
.menu-item{position:absolute;top:42px;font-family:"Barlow",sans-serif;font-weight:600;font-size:17px;color:var(--white);white-space:nowrap}
.book-btn{position:absolute;left:953px;top:26px;width:178px;height:53px;background:var(--gold);color:var(--white);font-family:"Barlow",sans-serif;font-weight:600;font-size:14px;display:flex;align-items:center;justify-content:center;gap:10px}
.hero-title{position:absolute;left:0;width:1200px;top:205px;text-align:center;font-family:"Barlow",sans-serif;font-weight:500;font-size:41px;color:var(--white)}
.crumbs{position:absolute;left:0;width:1200px;top:268px;text-align:center;font-family:"Barlow",sans-serif;font-weight:600;font-size:12px;color:var(--white)}
.crumbs em{font-style:normal;color:var(--gold);font-weight:500}

/* intro */
.kicker{position:absolute;left:0;width:1200px;text-align:center;font-family:"Barlow",sans-serif;font-weight:600;font-size:13px;color:var(--gold)}
.section-title{position:absolute;left:0;width:1200px;text-align:center;font-size:41px;line-height:53px}
.intro-text{position:absolute;left:222px;width:756px;top:648px;text-align:center;font-size:13px;line-height:23px}
.photo{position:absolute}
.lobby{left:110px;top:764px;width:980px;height:350px;background:linear-gradient(110deg,#2a2220 0%,#5a4c44 35%,#8d8a86 65%,#b7b3ad 100%)}

/* amenities */
.card{position:absolute;top:1220px;width:229px;height:252px;background:var(--white);box-shadow:0 10px 30px rgba(0,0,0,.07);padding:36px 0 0 36px}
.card svg{display:block;width:56px;height:56px}
.card h3{margin-top:26px;font-size:22px;white-space:nowrap}
.card p{margin-top:12px;width:154px;font-size:13px;line-height:23px}

/* gallery */
.room{top:1578px;width:284px;height:284px}

/* team */
.member{position:absolute;top:2101px;width:312px;height:333px;background:linear-gradient(180deg,#e4e6ea,#d3d6dc)}
.member-tag{position:absolute;left:22px;top:210px;width:268px;height:101px;background:var(--white);text-align:center;padding-top:26px}
.member-tag h4{font-size:18px}
.member-tag span{display:block;margin-top:6px;font-size:13px;color:var(--gold)}

/* footer */
.footer{position:absolute;left:0;top:2540px;width:1200px;height:430px;background:var(--dark);color:var(--white)}
.footer .brand{left:110px;top:66px;font-size:28px}
.foot-about{position:absolute;left:110px;top:132px;width:230px;font-size:13px;line-height:23px;color:var(--foot-text)}
.socials{position:absolute;left:110px;top:203px;display:flex;gap:12px}
.socials span{width:35px;height:35px;border:1px solid rgba(255,255,255,.25);border-radius:50%}
.col-title{position:absolute;top:81px;font-family:"Barlow",sans-serif;font-weight:500;font-size:18px}
.info{position:absolute;left:360px;top:132px;font-size:13px;line-height:23px;color:var(--foot-text)}
.info-row{display:flex;gap:16px;margin-bottom:14px}
.info-row svg{flex:none;width:24px;height:24px}
.links{position:absolute;left:611px;top:127px;font-size:13px;color:var(--foot-text);line-height:32px}
.subscribe{position:absolute;left:778px;top:136px;width:312px;height:61px;border:1px solid rgba(255,255,255,.15);display:flex}
.subscribe span{flex:1;padding:22px 18px;font-size:13px;color:#8a8e95}
.subscribe b{width:61px;background:var(--gold);display:flex;align-items:center;justify-content:center}
.foot-rule{position:absolute;left:0;top:335px;width:1200px;height:1px;background:var(--line)}
.copy{position:absolute;left:110px;top:376px;font-size:13px}
.copy em{font-style:normal;color:var(--gold)}
.legal{position:absolute;right:110px;top:376px;font-size:13px;display:flex;gap:12px}
.legal i{font-style:normal;color:rgba(255,255,255,.45)}
.to-top{position:absolute;left:1138px;top:362px;width:44px;height:44px;border:1.5px solid var(--gold);border-radius:50%;display:flex;align-items:center;justify-content:center}
</style>
</head>
<body>

<header class="hero">
  <div class="nav-bar"></div>
  <div class="brand"><span class="brand-mark"></span>Corvena Hotel</div>
  <nav>
    <span class="menu-item" style="left:331px">Home +</span>
    <span class="menu-item" style="left:438px">Pages +</span>
    <span class="menu-item" style="left:548px">Room +</span>
    <span class="menu-item" style="left:654px">Blog +</span>
    <span class="menu-item" style="left:753px">Contact</span>
  </nav>
  <div class="book-btn">BOOK NOW
    <svg width="16" height="10" viewBox="0 0 16 10" fill="none" stroke="#fff" stroke-width="1.6"><path d="M0 5h14M10 1l4 4-4 4"/></svg>
  </div>
  <h1 class="hero-title">About Us</h1>
  <div class="crumbs">Home&nbsp; - &nbsp;<em>About Us</em></div>
</header>

<section>
  <div class="kicker" style="top:505px">Company Offers</div>
  <h2 class="section-title heading" style="top:530px">Book now and save up to 35%<br>On hotel rooms</h2>
  <p class="intro-text">hasellus nisi sapien, rutrum placerat sapien eu, rhoncus tempus felis. Nulla non pulvinar enim, vel viverra nunc. Integer condimentum vulputate justo. Morbi rhoncus elit in tellus viverra, vel fermentum orci dictum. Vestibulum non nisi commodo, tincidunt elit non, consectetur tellus. Fusce in commodo velit. In dapibus dui vitae tortor ullamcorper mollis.</p>
  <div class="photo lobby" role="img" aria-label="Guests checking in at the hotel reception desk"></div>
</section>

<section>
  <div class="card" style="left:110px">
    <svg viewBox="0 0 56 56" fill="none" stroke="#bd9343" stroke-width="1.6"><path d="M26 4v26M20 30h12l4 22H16z"/><path d="M38 36h12v16H38zM41 36v-5h6v5"/><path d="M8 20l2 4 4 1-4 2-2 4-2-4-4-2 4-1z"/></svg>
    <h3 class="heading">Room Cleaning</h3>
    <p>Proin massa augue, lacinia at blandit ac, Fringilla scelerisque tortor. Mauris</p>
  </div>
  <div class="card" style="left:360px">
    <svg viewBox="0 0 56 56" fill="none" stroke="#bd9343" stroke-width="1.6"><path d="M4 40h38v-8l-6-2-5-7H14l-6 7-4 2z"/><circle cx="13" cy="41" r="4"/><circle cx="33" cy="41" r="4"/><rect x="38" y="4" width="14" height="14"/><path d="M43 15V8h3a2 2 0 010 4h-3M45 18v14"/></svg>
    <h3 class="heading">Car Parking</h3>
    <p>Proin massa augue, lacinia at blandit ac, Fringilla scelerisque tortor. Mauris</p>
  </div>
  <div class="card" style="left:610px">
    <svg viewBox="0 0 56 56" fill="none" stroke="#bd9343" stroke-width="1.6"><path d="M14 38V14a6 6 0 0112 0M32 38V14a6 6 0 0112 0M14 22h18M14 30h18"/><path d="M4 44c4-3 8 3 12 0s8 3 12 0 8 3 12 0 8 3 12 0"/></svg>
    <h3 class="heading">Swimming pool</h3>
    <p>Proin massa augue, lacinia at blandit ac, Fringilla scelerisque tortor. Mauris</p>
  </div>
  <div class="card" style="left:861px">
    <svg viewBox="0 0 56 56" fill="none" stroke="#bd9343" stroke-width="1.6"><path d="M28 36S16 24 16 15a12 12 0 0124 0c0 9-12 21-12 21z"/><circle cx="28" cy="15" r="5"/><path d="M14 34L4 52l16-6 16 6 16-6-10-12"/></svg>
    <h3 class="heading">PickUp &amp; Drop</h3>
    <p>Proin massa augue, lacinia at blandit ac, Fringilla scelerisque tortor. Mauris</p>
  </div>
</section>

<section>
  <div class="photo room" style="left:0;background:linear-gradient(135deg,#c9a476,#55585c 60%,#6f8a7a)" role="img" aria-label="Bedroom with grey headboard and green throw"></div>
  <div class="photo room" style="left:305px;background:linear-gradient(135deg,#e8e2d6,#d9c7a0 50%,#a79f92)" role="img" aria-label="Bright bedroom with wooden floor"></div>
  <div class="photo room" style="left:610px;background:linear-gradient(135deg,#7a6f6a,#b7aca3 50%,#8c8580)" role="img" aria-label="Lounge with sofa and round coffee table"></div>
  <div class="photo room" style="left:916px;background:linear-gradient(135deg,#8f8b86,#4a5575 55%,#b18c6b)" role="img" aria-label="Living area with blue sofa and dining table"></div>
</section>

<section>
  <div class="kicker" style="top:1972px">Our Exprt Meamber</div>
  <h2 class="section-title heading" style="top:1997px">Expert Our Services man</h2>
  <div class="member" style="left:110px" role="img" aria-label="Portrait of a services team member">
    <div class="member-tag"><h4 class="heading">Elena Marou</h4><span>Services man</span></div>
  </div>
  <div class="member" style="left:444px" role="img" aria-label="Portrait of a services team member">
    <div class="member-tag"><h4 class="heading">Nikos Daranis</h4><span>Services man</span></div>
  </div>
  <div class="member" style="left:778px" role="img" aria-label="Portrait of a services team member">
    <div class="member-tag"><h4 class="heading">Sofia Kalend</h4><span>Services man</span></div>
  </div>
</section>

<footer class="footer">
  <div class="brand"><span class="brand-mark"></span>Corvena Hotel</div>
  <p class="foot-about">Phasellus nisi sapien, rutrum placerat sapien eu, rhoncus tempus</p>
  <div class="socials">
    <span aria-label="Social link one"></span><span aria-label="Social link two"></span><span aria-label="Social link three"></span><span aria-label="Social link four"></span>
  </div>

  <div class="col-title" style="left:360px">Information</div>
  <div class="info">
    <div class="info-row"><svg viewBox="0 0 24 24" fill="none" stroke="#bd9343" stroke-width="1.4"><path d="M12 14s-5-5-5-8a5 5 0 0110 0c0 3-5 8-5 8z"/><path d="M6 12l-4 10 7-3 6 3 7-3-4-7"/></svg><span>Odos Lindou 12 Rhodes,<br>Greece</span></div>
    <div class="info-row"><svg viewBox="0 0 24 24" fill="none" stroke="#bd9343" stroke-width="1.4"><rect x="2" y="6" width="20" height="14"/><path d="M2 6l10 8 10-8"/></svg><span>stay@corvena-mail.com</span></div>
    <div class="info-row"><svg viewBox="0 0 24 24" fill="none" stroke="#bd9343" stroke-width="1.4"><path d="M5 2l4 1 1 5-3 2a12 12 0 007 7l2-3 5 1 1 4c-1 2-3 3-5 3C10 21 3 14 2 7c0-2 1-4 3-5z"/></svg><span>+30 (224) 100 2200</span></div>
  </div>

  <div class="col-title" style="left:610px">Pages Links</div>
  <div class="links">Room Cleaning<br>Car Parking<br>Swimming pool<br>Fitness Gym</div>

  <div class="col-title" style="left:777px">Subscribe</div>
  <div class="subscribe"><span>Email Address</span><b><svg width="16" height="16" viewBox="0 0 16 16" fill="none" stroke="#fff" stroke-width="1.5"><path d="M1 8l14-6-5 13-3-5z"/></svg></b></div>

  <div class="foot-rule"></div>
  <div class="copy">Copyright 2022 <em>Corvena Hotel</em>, All rights reserved.</div>
  <div class="legal"><span>FAQ</span><i>|</i><span>Terms of Use</span><i>|</i><span>Privacy Policy</span></div>
  <div class="to-top"><svg width="12" height="16" viewBox="0 0 12 16" fill="none" stroke="#bd9343" stroke-width="1.5"><path d="M6 16V2M1 6l5-5 5 5"/></svg></div>
</footer>

</body>
</html>
```